Redesign my business cards

I would like pretty much all the same information as my current business cards but redesigned to stand out more and be more unique photo uploaded to show my current business cards don’t mind if you want to remove or replace I for on the back

```html
<!DOCTYPE html>
<html lang="en">
<head>
<meta charset="utf-8">
<title>Velmont Detailing – Business Cards</title>
<link href="https://fonts.googleapis.com/css2?family=Bebas+Neue&family=Montserrat:wght@400;500;600&family=Oswald:wght@400;500&display=swap" rel="stylesheet">
<style>
  :root{
    --backdrop:#2c2d2f;
    --card:#062a3d;
    --card-light:#0d3a52;
    --accent-blue:#3d8fe6;
    --accent-cyan:#3fb8e6;
    --accent-purple:#8a5cf0;
    --text-white:#f2f6f9;
  }
  *{margin:0;padding:0;box-sizing:border-box}
  html,body{width:1200px;height:1200px;overflow:hidden;background:var(--backdrop)}
  .stage{width:1200px;height:1200px;display:flex;flex-direction:column;align-items:center;justify-content:center;gap:52px}
  .card{
    position:relative;width:900px;height:514px;border-radius:44px;
    background:linear-gradient(100deg,var(--card) 0%,var(--card) 48%,var(--card-light) 56%,var(--card) 66%,var(--card) 100%);
    box-shadow:0 14px 30px rgba(0,0,0,.45);overflow:hidden;
  }
  .brand{position:absolute;display:flex;flex-direction:column;align-items:center;gap:18px;width:300px}
  .brand-dot{width:70px;height:70px;border-radius:50%;background:var(--accent-cyan)}
  .brand-name{font-family:'Montserrat',sans-serif;font-weight:600;font-size:26px;letter-spacing:5px;color:var(--accent-purple);text-align:center;line-height:1.3}
  .card-front .brand{left:70px;top:160px}
  .card-back .brand{right:70px;top:160px}

  .contact{position:absolute;left:470px;top:150px}
  .contact-name{font-family:'Montserrat',sans-serif;font-weight:500;font-size:44px;color:var(--accent-blue);letter-spacing:.5px;line-height:1}
  .contact-role{font-family:'Montserrat',sans-serif;font-weight:400;font-size:22px;color:var(--text-white);letter-spacing:1px;margin-top:8px}
  .contact-list{list-style:none;margin-top:34px;display:flex;flex-direction:column;gap:14px}
  .contact-item{display:flex;align-items:center;gap:14px;font-family:'Oswald',sans-serif;font-weight:500;font-size:26px;color:var(--text-white);text-transform:uppercase}
  .contact-item svg{width:26px;height:26px;flex:none}

  .price-list{position:absolute;left:56px;top:70px;width:520px;display:flex;flex-direction:column;gap:30px}
  .service-head{display:flex;align-items:center;gap:12px}
  .service-title{font-family:'Bebas Neue',sans-serif;font-size:32px;color:var(--accent-blue);letter-spacing:.5px;white-space:nowrap}
  .service-rule{flex:1;height:2px;background:var(--accent-cyan)}
  .service-price{font-family:'Bebas Neue',sans-serif;font-size:36px;color:var(--accent-blue)}
  .service-desc{font-family:'Oswald',sans-serif;font-weight:400;font-size:15px;line-height:1.35;color:var(--text-white);text-transform:uppercase;margin-top:2px}
</style>
</head>
<body>
<main class="stage">
  <section class="card card-front">
    <div class="brand">
      <span class="brand-dot"></span>
      <span class="brand-name">VELMONT<br>DETAILING</span>
    </div>
    <div class="contact">
      <h1 class="contact-name">DANIEL WHITMORE</h1>
      <p class="contact-role">OWNER | OPERATOR</p>
      <ul class="contact-list">
        <li class="contact-item">
          <svg viewBox="0 0 24 24" aria-hidden="true"><path fill="#3d8fe6" d="M6.6 10.8a15.1 15.1 0 0 0 6.6 6.6l2.2-2.2c.3-.3.7-.4 1-.2 1.1.4 2.3.6 3.6.6.6 0 1 .4 1 1V20c0 .6-.4 1-1 1A17 17 0 0 1 3 4c0-.6.4-1 1-1h3.5c.6 0 1 .4 1 1 0 1.3.2 2.5.6 3.6.1.3 0 .7-.2 1z"/></svg>
          0455218604
        </li>
        <li class="contact-item">
          <svg viewBox="0 0 24 24" aria-hidden="true"><rect x="2" y="5" width="20" height="14" rx="1" fill="#3d8fe6"/><path d="M2 6l10 7 10-7" fill="none" stroke="#062a3d" stroke-width="1.6"/></svg>
          velmontdetailing@mailbox.com
        </li>
      </ul>
    </div>
  </section>

  <section class="card card-back">
    <div class="price-list">
      <article class="service">
        <div class="service-head"><h2 class="service-title">INTERIOR DETAIL</h2><span class="service-rule"></span><span class="service-price">$150</span></div>
        <p class="service-desc">Vacume &amp; deep clean of carpets &amp; upholstery<br>or leather treatment, interior trim clean &amp; condition,<br>window polish and treatment, steam clean and stain removal</p>
      </article>
      <article class="service">
        <div class="service-head"><h2 class="service-title">EXTERIOR DETAIL</h2><span class="service-rule"></span><span class="service-price">$250</span></div>
        <p class="service-desc">Extreme wash &amp; polish, exterior trim reviver &amp; protector<br>window polish &amp; treatment, tyre dressing, engine bay cleaned</p>
      </article>
      <article class="service">
        <div class="service-head"><h2 class="service-title">FULL EXTREME DETAIL</h2><span class="service-rule"></span><span class="service-price">$350</span></div>
        <p class="service-desc">Vacume &amp; deep clean of carpets &amp; upholstery<br>or leather treatment, interior trim clean &amp; condition,<br>window polish and treatment, steam clean and stain removal</p>
      </article>
    </div>
    <div class="brand">
      <span class="brand-dot"></span>
      <span class="brand-name">VELMONT<br>DETAILING</span>
    </div>
  </section>
</main>
</body>
</html>
```